Logo and business card for optometric practice
Calvin Mortenhall & Associates
Petra Valunkova, O.D.
Simon Orchardt, O.D.
Neil Tabarrou, O.D.
417 Meadowbrook Parkway
Ashfield Terrace, New York 11498
516-555-0142

Target Market(s)

Patients, general public

Industry/Entity Type

Business

Logo Text

Calvin Mortenhall & Associates Optometrists

Logo styles of interest
Pictorial/Combination Logo
Font styles to use
Serif
Sans Serif

Requirements
Must have
• current inspiration: realistic or photo closeup of eye, with interesting treatment of the iris OR
tech look, with closeup of eye and grid like the doctor is looking through a camera or microscope to view the eye up close
Should not have
• NO cartoons

```html
<!DOCTYPE html>
<html lang="en">
<head>
<meta charset="utf-8">
<title>Calvin Mortenhall &amp; Associates – Business Card</title>
<link rel="stylesheet" href="https://fonts.googleapis.com/css2?family=Arimo:wght@700&family=Questrial&display=swap">
<style>
  :root {
    --page-bg: #e6e4e0;
    --card-front: #eceeed;
    --card-back: #ffffff;
    --slate: #6c7a7d;
    --mint: #8ef5b8;
    --shadow: rgba(0, 0, 0, 0.18);
  }
  * { margin: 0; padding: 0; box-sizing: border-box; }
  html, body {
    width: 1200px;
    height: 1000px;
    overflow: hidden;
    background: var(--page-bg);
  }
  .canvas {
    position: relative;
    width: 1200px;
    height: 1000px;
  }
  .card {
    position: absolute;
    width: 800px;
    height: 430px;
    border-radius: 26px;
    box-shadow: 0 10px 28px var(--shadow);
  }
  .card--front {
    left: 100px;
    top: 60px;
    background: var(--card-front);
    display: flex;
    align-items: center;
    justify-content: center;
  }
  .card--back {
    left: 300px;
    top: 520px;
    background: var(--card-back);
  }

  /* Front: brand lockup */
  .brand {
    display: flex;
    align-items: center;
    gap: 26px;
  }
  .brand__dot {
    width: 70px;
    height: 70px;
    border-radius: 50%;
    background: var(--mint);
    flex: none;
  }
  .brand__name {
    font-family: "Arimo", Arial, sans-serif;
    font-weight: 700;
    font-size: 30px;
    line-height: 1.25;
    color: var(--slate);
  }

  /* Back: details */
  .practice {
    position: absolute;
    left: 50px;
    top: 40px;
    font-family: "Arimo", Arial, sans-serif;
    font-weight: 700;
    font-size: 27px;
    line-height: 1.2;
  }
  .practice__name { color: var(--slate); }
  .practice__type { color: var(--mint); }

  .mark {
    position: absolute;
    right: 46px;
    top: 130px;
    display: flex;
    align-items: center;
    gap: 12px;
  }
  .mark__dot {
    width: 40px;
    height: 40px;
    border-radius: 50%;
    background: var(--mint);
  }
  .mark__name {
    font-family: "Arimo", Arial, sans-serif;
    font-weight: 700;
    font-size: 16px;
    color: var(--slate);
  }

  .doctors, .address {
    position: absolute;
    font-family: "Questrial", "Century Gothic", sans-serif;
    font-size: 22px;
    line-height: 1.3;
    color: var(--slate);
    list-style: none;
  }
  .doctors { left: 50px; bottom: 55px; }
  .doctors .credential { color: var(--mint); }
  .address {
    right: 46px;
    bottom: 40px;
    text-align: right;
    font-style: normal;
  }
</style>
</head>
<body>
<main class="canvas">
  <section class="card card--front" aria-label="Card front">
    <div class="brand">
      <span class="brand__dot" aria-hidden="true"></span>
      <p class="brand__name">Calvin Mortenhall &amp; Associates<br>Optometrists</p>
    </div>
  </section>

  <section class="card card--back" aria-label="Card back">
    <header class="practice">
      <p class="practice__name">Calvin Mortenhall &amp; Associates</p>
      <p class="practice__type">optometric practice</p>
    </header>

    <div class="mark">
      <span class="mark__dot" aria-hidden="true"></span>
      <span class="mark__name">Calvin Mortenhall &amp; Associates</span>
    </div>

    <ul class="doctors">
      <li>Petra Valunkova, <span class="credential">O.D.</span></li>
      <li>Simon Orchardt, <span class="credential">O.D.</span></li>
      <li>Neil Tabarrou, <span class="credential">O.D.</span></li>
    </ul>

    <address class="address">
      417 Meadowbrook Parkway<br>
      Ashfield Terrace,<br>
      New York 11498<br>
      P:516-555-0142
    </address>
  </section>
</main>
</body>
</html>
```